Law Firm Advertising Design Needed

Law Office of Dorvel K Tansy provides legal services to businesses and individuals who have been or are being injured. Our main practice area is personal injury (car accidents, wrongful death, premises liability), but we are looking for an ad that highlights a lesser known area of our practice - insurance company bad faith and breach of contract.

This ad will be placed in 8 1/2" x 11" format in a local neighborhood directory. It will also be placed in a smaller format (to be determined) in the local newspaper of a region of Arizona that has recently lost a considerable number of homes and people to wildfire.

We want to convey through the ad that our firm is available to help if their insurance company is not paying a legitimate claim or not paying enough for their claim.

Because of the tragic nature of the events in Yarnell, we would like to avoid images of fire or anything resembling fire. However, the ad should capture the attention of individuals who are struggling through an insurance claim with all the stacks of paperwork and frustrated with unresponsive adjusters and unreasonably low offers.

The design should convey a feeling of safety, security and being taken care of.

Information that must be included in the ad are: the firm name (Law Office of Dorvel K Tansy), address (4857 W 17th Avenue, Ste 406, Phoenix, AZ 85033), the phone number (602-574-2930) and the fact that we have mobile offices available to assist in your area.

An example of text that has been used in the past is here:
"If your own insurance company is refusing to pay what you are owed on a claim, call the Law Office of Dorvel K Tansy. We fight for you by examining the reasons your insurance carrier is denying or making an insufficient offer on the claim; updating and correcting claim documentation; making a new demand and filing a lawsuit if necessary. Whether it's a simple misunderstanding or something more complicated, we can help!

Here are a few of the kinds of claims we handle:
- Hit and Run or Uninsured driver claims
- Fire, flood and property loss
- Life insurance benefits
- Health insurance claims
- Catastrophic losses
- Business insurance
- Wrongful Death Benefits

Our attorneys are available to help you cut through the nonsense. Call to make an appointment for a free consultation with an attorney today. "

An example of a previous ad for car accident services is attached for reference.
Updates

Hi Everyone,

The main lawyer involved in the decision making process has been giving me some feedback in general on the designs that I thought I would pass along.  He does not want the name of the law firm to be the first thing you notice when you look at the ad. Try to keep that small and possibly to the bottom of the ad. The phone number should be rather large, but the address should be rather small (we are required by the State Bar to include our address, but we don't want our location to limit the location of our clients because our mobile offices can travel to them).  He would prefer that the logo either not be included or be not a significant part of the ad.

                                   

Thanks!  I will continue providing individual feedback to ads received. 

Target Market(s)

Low to middle income residents of the State of Arizona with little or no college education

Industry/Entity Type

Insurance

```html
<!DOCTYPE html>
<html lang="en">
<head>
<meta charset="utf-8">
<title>Law Office of Dorvel K Tansy – Insurance Claims Ad</title>
<link rel="stylesheet" href="https://fonts.googleapis.com/css2?family=Montserrat:wght@400;500;600;700&display=swap">
<style>
  :root {
    --royal: #1f56d6;
    --royal-deep: #0b34a8;
    --sky: #4f8cf0;
    --pale: #c9d9f7;
    --pale-mid: #b3c8f1;
    --ink: #0c0c14;
    --white: #ffffff;
    --photo-dark: #2a2020;
    --photo-mid: #6a5548;
  }
  * { margin: 0; padding: 0; box-sizing: border-box; }
  html, body { width: 844px; height: 1200px; overflow: hidden; background: #ffffff; }
  body { font-family: "Montserrat", Arial, sans-serif; color: var(--ink); }

  .ad { position: relative; width: 844px; height: 1200px; overflow: hidden;
        background: linear-gradient(180deg, var(--pale) 0%, #d6e2f8 45%, var(--pale-mid) 78%); }

  /* Header */
  .hero { position: absolute; left: 0; top: 0; width: 844px; height: 437px;
          background: radial-gradient(ellipse at 30% 40%, var(--sky) 0%, var(--royal) 45%, var(--royal-deep) 100%);
          overflow: hidden; }
  .hero-photo { position: absolute; right: 0; top: 0; width: 450px; height: 437px;
                background: linear-gradient(90deg, rgba(31,86,214,0) 0%, rgba(70,60,70,0.85) 22%, var(--photo-mid) 45%, var(--photo-dark) 100%); }
  .hero-arc { position: absolute; left: 0; top: 0; }
  .hero-headline { position: absolute; left: 56px; top: 198px; color: var(--white);
                   font-size: 40px; font-weight: 500; line-height: 1.35; letter-spacing: 0.3px; }
  .web-address { position: absolute; right: 58px; top: 44px; color: var(--white);
                 font-size: 14px; font-weight: 600; }

  /* Intro */
  .intro { position: absolute; left: 50px; top: 466px; width: 745px;
           font-size: 14.4px; line-height: 1.45; font-weight: 500; }
  .intro strong { font-size: 19px; font-weight: 700; }

  /* Claims */
  .claims-title { position: absolute; left: 48px; top: 628px; font-size: 23px; font-weight: 700; }
  .claims-list { position: absolute; left: 48px; top: 664px; width: 760px; list-style: none;
                 display: grid; grid-template-columns: 440px 320px; row-gap: 4px;
                 font-size: 20px; font-weight: 500; }
  .claims-list li { display: flex; align-items: center; gap: 10px; }
  .bullet { width: 16px; height: 16px; flex: none; }

  .swoosh { position: absolute; left: 0; top: 800px; }

  .call-to-action { position: absolute; left: 0; width: 844px; top: 902px; text-align: center;
                    font-size: 19px; font-weight: 500; line-height: 1.4; }

  /* Footer */
  .footer { position: absolute; left: 0; top: 975px; width: 844px; height: 225px;
            background: linear-gradient(180deg, rgba(31,86,214,0) 0%, var(--royal) 28%, var(--royal-deep) 100%); }
  .brand { position: absolute; left: 150px; top: 1022px; width: 140px; text-align: center; color: var(--white); }
  .brand-square { width: 84px; height: 84px; background: var(--white); margin: 0 auto 10px; }
  .brand-name { font-size: 22px; font-weight: 600; }
  .firm { position: absolute; left: 330px; top: 1020px; color: var(--white); font-style: normal; }
  .firm-name { font-size: 20px; font-weight: 700; }
  .firm-address { font-size: 13.5px; font-weight: 500; margin-top: 4px; }
  .firm-phone { font-size: 42px; font-weight: 500; margin-top: 6px; letter-spacing: 0.5px; line-height: 1.15; }
  .mobile-offices { font-size: 15px; font-weight: 600; margin-top: 6px; }
</style>
</head>
<body>
<main class="ad">
  <header class="hero">
    <svg class="hero-arc" width="844" height="437" viewBox="0 0 844 437" aria-hidden="true">
      <path d="M-40 150 C 180 60, 420 70, 620 140" stroke="rgba(255,255,255,0.25)" stroke-width="3" fill="none"/>
      <path d="M-40 175 C 200 90, 430 100, 640 170" stroke="rgba(255,255,255,0.15)" stroke-width="2" fill="none"/>
    </svg>
    <div class="hero-photo" role="img" aria-label="Photograph of the attorney in a dark suit seated at his office desk"></div>
    <p class="web-address">www.tansylawoffice.com</p>
    <h1 class="hero-headline">Any Accident,<br>Any Injury…<br>Let us fight for you!</h1>
  </header>

  <p class="intro"><strong>If your own insurance company is refusing to pay</strong> what you are owed on a claim, call the Law Office of Dorvel K Tansy. We fight for you by examining the reasons your insurance carrier is denying or making an insufficient offer on the claim; updating and correcting claim documentation; making a new demand and filing a lawsuit if necessary. Whether it's a simple misunderstanding or something more complicated, we can help!</p>

  <h2 class="claims-title">Here are a few of the kinds of claims we handle :</h2>
  <ul class="claims-list">
    <li><svg class="bullet" viewBox="0 0 16 16"><path d="M8 1 L15 8 L8 15 L1 8 Z" fill="none" stroke="#0c0c14" stroke-width="1.6"/><path d="M8 5 L11 8 L8 11 L5 8 Z" fill="#0c0c14"/></svg>Hit and Run or Uninsured driver claims</li>
    <li><svg class="bullet" viewBox="0 0 16 16"><path d="M8 1 L15 8 L8 15 L1 8 Z" fill="none" stroke="#0c0c14" stroke-width="1.6"/><path d="M8 5 L11 8 L8 11 L5 8 Z" fill="#0c0c14"/></svg>Fire, flood and property loss</li>
    <li><svg class="bullet" viewBox="0 0 16 16"><path d="M8 1 L15 8 L8 15 L1 8 Z" fill="none" stroke="#0c0c14" stroke-width="1.6"/><path d="M8 5 L11 8 L8 11 L5 8 Z" fill="#0c0c14"/></svg>Life insurance benefits</li>
    <li><svg class="bullet" viewBox="0 0 16 16"><path d="M8 1 L15 8 L8 15 L1 8 Z" fill="none" stroke="#0c0c14" stroke-width="1.6"/><path d="M8 5 L11 8 L8 11 L5 8 Z" fill="#0c0c14"/></svg>Health insurance claims</li>
    <li><svg class="bullet" viewBox="0 0 16 16"><path d="M8 1 L15 8 L8 15 L1 8 Z" fill="none" stroke="#0c0c14" stroke-width="1.6"/><path d="M8 5 L11 8 L8 11 L5 8 Z" fill="#0c0c14"/></svg>Catastrophic losses</li>
    <li><svg class="bullet" viewBox="0 0 16 16"><path d="M8 1 L15 8 L8 15 L1 8 Z" fill="none" stroke="#0c0c14" stroke-width="1.6"/><path d="M8 5 L11 8 L8 11 L5 8 Z" fill="#0c0c14"/></svg>Business insurance</li>
    <li><svg class="bullet" viewBox="0 0 16 16"><path d="M8 1 L15 8 L8 15 L1 8 Z" fill="none" stroke="#0c0c14" stroke-width="1.6"/><path d="M8 5 L11 8 L8 11 L5 8 Z" fill="#0c0c14"/></svg>Wrongful Death Benefits</li>
  </ul>

  <svg class="swoosh" width="844" height="120" viewBox="0 0 844 120" aria-hidden="true">
    <path d="M60 90 C 260 10, 560 0, 844 40" stroke="rgba(255,255,255,0.8)" stroke-width="3" fill="none"/>
    <path d="M140 100 C 320 35, 580 25, 844 60" stroke="rgba(90,110,220,0.45)" stroke-width="4" fill="none"/>
    <path d="M0 115 C 240 60, 560 50, 844 85" stroke="rgba(255,255,255,0.5)" stroke-width="2" fill="none"/>
  </svg>

  <p class="call-to-action">Our attorneys are available to help you cut through the nonsense.<br>Call to make an appointment for a free consultation with an attorney today.</p>

  <footer class="footer"></footer>
  <div class="brand">
    <div class="brand-square"></div>
    <p class="brand-name">Tansy Law</p>
  </div>
  <address class="firm">
    <p class="firm-name">Law Office of Dorvel K Tansy</p>
    <p class="firm-address">(4857 W 17th Avenue, Ste 406, Phoenix, AZ 85033)</p>
    <p class="firm-phone">(602) 574 2930</p>
    <p class="mobile-offices">Mobile offices available to assist in your area.</p>
  </address>
</main>
</body>
</html>
```